Professional Business Cards for Recruiting Company

We'd like professional 2-sided business cards that reflect a color scheme that matches our website, www.quillmerbay.com, and / or logo that is attached.

Slogan used is "We Find Talent", but needs to be editable because we change it up to "We Know Developers", "We Speak Geek", etc.

Must includes logo, slogan, first and last name, address, email, mobile number and website address.

Files attached for ideas.

Thanks!

Contact Information for Business Card

Logo, Company name, First name, Last name, addresss, email, phone, website address.

Font styles to use
Sans Serif

Colors
0054AA
0677BA
7BADD7
CADEEF
E8F1F8

Requirements
Nice to have
• I do like the following designs. 22962062 and 22962651. Couple ideas anyway.

```html
<!DOCTYPE html>
<html lang="en">
<head>
<meta charset="utf-8">
<title>Quillmerbay Business Card</title>
<link href="https://fonts.googleapis.com/css2?family=Montserrat:wght@300;400;500;600;700&display=swap" rel="stylesheet">
<style>
  :root {
    --backdrop: #a8a8a8;
    --card: #222326;
    --ink: #ffffff;
    --ink-soft: #e6e6e6;
  }
  * { margin: 0; padding: 0; box-sizing: border-box; }
  html, body { width: 1200px; height: 1063px; overflow: hidden; }
  body {
    background: var(--backdrop);
    font-family: "Montserrat", sans-serif;
    color: var(--ink);
    position: relative;
  }
  .card {
    position: absolute;
    left: 299px;
    width: 599px;
    height: 342px;
    background: var(--card);
  }
  .card--front { top: 189px; }
  .card--back { top: 581px; }

  .brand-mark {
    display: flex;
    align-items: center;
    gap: 8px;
    color: var(--ink);
    white-space: nowrap;
  }
  .brand-mark__square {
    width: 12px; height: 12px;
    background: var(--ink);
    flex: none;
  }
  .card--front .brand-mark {
    position: absolute;
    left: 176px; top: 149px;
    transform: translateX(-50%);
    font-size: 16px;
    font-weight: 600;
    letter-spacing: 0.6px;
    line-height: 1;
  }
  .slogan {
    position: absolute;
    left: 178px; top: 227px;
    transform: translateX(-50%);
    font-size: 12px;
    font-weight: 600;
    letter-spacing: 0.3px;
    line-height: 1;
    white-space: nowrap;
  }
  .person-name {
    position: absolute;
    left: 270px; top: 99px;
    font-size: 23px;
    font-weight: 600;
    letter-spacing: 0.8px;
    line-height: 1.2;
  }
  .person-role {
    position: absolute;
    left: 270px; top: 127px;
    font-size: 13px;
    font-weight: 400;
    line-height: 1.2;
    color: var(--ink-soft);
  }
  .contact-rail {
    position: absolute;
    left: 270px; top: 158px;
    width: 18px; height: 85px;
    background: var(--ink);
    border-radius: 9px 9px 0 0;
  }
  .contact-rule {
    position: absolute;
    left: 270px; top: 241px;
    right: 0;
    height: 2px;
    background: var(--ink);
  }
  .contact-list { list-style: none; }
  .contact-item {
    position: absolute;
    left: 296px;
    font-size: 14px;
    font-weight: 400;
    line-height: 16px;
    white-space: nowrap;
  }
  .contact-icon {
    position: absolute;
    left: 272px;
    width: 14px; height: 14px;
  }

  .brand-lockup {
    position: absolute;
    left: 50%; top: 146px;
    transform: translateX(-50%);
    display: flex;
    flex-direction: column;
    align-items: center;
  }
  .card--back .brand-mark {
    font-size: 30px;
    font-weight: 300;
    letter-spacing: 1px;
    line-height: 1.1;
  }
  .card--back .brand-mark__square { width: 14px; height: 14px; }
  .brand-descriptor {
    margin-top: 4px;
    padding-top: 4px;
    border-top: 1px solid var(--ink);
    font-size: 8px;
    font-weight: 700;
    letter-spacing: 1.2px;
    line-height: 1;
    white-space: nowrap;
  }
</style>
</head>
<body>

<section class="card card--front">
  <div class="brand-mark"><span class="brand-mark__square"></span>QUILLMERBAY</div>
  <p class="slogan">WE FIND TALENT</p>

  <h1 class="person-name">MARA ELLISON</h1>
  <p class="person-role">CEO/Owner</p>

  <div class="contact-rail"></div>
  <div class="contact-rule"></div>

  <svg class="contact-icon" style="top:160px" viewBox="0 0 14 14" aria-hidden="true">
    <circle cx="7" cy="7" r="7" fill="#222326"/>
    <path d="M4.3 3.6l1.5-.3.8 2-1 .8a5.5 5.5 0 0 0 2.4 2.4l.8-1 2 .8-.3 1.5c-3.6.2-6.4-2.6-6.2-6.2z" fill="#fff"/>
  </svg>
  <svg class="contact-icon" style="top:181px" viewBox="0 0 14 14" aria-hidden="true">
    <circle cx="7" cy="7" r="7" fill="#222326"/>
    <rect x="3.5" y="4.5" width="7" height="5" fill="none" stroke="#fff" stroke-width="1"/>
    <path d="M3.5 4.5L7 7.5l3.5-3" fill="none" stroke="#fff" stroke-width="1"/>
  </svg>
  <svg class="contact-icon" style="top:201px" viewBox="0 0 14 14" aria-hidden="true">
    <circle cx="7" cy="7" r="7" fill="#222326"/>
    <circle cx="7" cy="7" r="3.6" fill="none" stroke="#fff" stroke-width="0.9"/>
    <ellipse cx="7" cy="7" rx="1.5" ry="3.6" fill="none" stroke="#fff" stroke-width="0.8"/>
    <path d="M3.4 7h7.2" stroke="#fff" stroke-width="0.8"/>
  </svg>
  <svg class="contact-icon" style="top:221px" viewBox="0 0 14 14" aria-hidden="true">
    <circle cx="7" cy="7" r="7" fill="#222326"/>
    <path d="M3.5 7.3L7 4l3.5 3.3h-1v3H4.5v-3z" fill="#fff"/>
  </svg>

  <ul class="contact-list">
    <li class="contact-item" style="top:159px">123-456-7899</li>
    <li class="contact-item" style="top:180px">info@quillmerbay.com</li>
    <li class="contact-item" style="top:200px">www.quillmerbay.com</li>
    <li class="contact-item" style="top:220px">123, Your Street Name, 12 city</li>
  </ul>
</section>

<section class="card card--back">
  <div class="brand-lockup">
    <div class="brand-mark"><span class="brand-mark__square"></span>QUILLMERBAY</div>
    <p class="brand-descriptor">TALENT SEARCH AND STAFFING PARTNERS</p>
  </div>
</section>

</body>
</html>
```